Presentation Folder, for Cancer Awareness, VERY COLORFULL AND MODERN

This will be a standard size folder that will hold standard 8 1/2 x 11 papers with a business card slot on the flap, this is a very easy project with very little text and the design for the back page is already done so all you really have to do is make a very nice colorful front cover, you will see my attachments are labeled and I gave you alot of instructions, this should be a very fast easy project
Updates

Reason: there has not been enough quality designs, sorry

Target Market(s)

Our Target Market is Dr's that Deal with Cancer patients

Industry/Entity Type

Healthcare

Font styles to use
Serif

Colors

Designer to choose colors to be used in the design.

Requirements
Must have
• Project must be tasteful and look professional with the ribbons as the main focal point in the center of folder the folder should be a nice gray color to accent the color of the ribbons , the back page needs no design it is the" Velmora Test" in the attachments I sent
Nice to have
• I would like the ribbons displayed in a row, I included a logo sample layout
• a picture on the front of the folder under the words Hereditary Cancer Screening - Then under that put the words - The Power of Knowledge - then add the picture I labeled Great Picture in the attachments

```html
<!DOCTYPE html>
<html lang="en">
<head>
<meta charset="utf-8">
<title>Genevora Hereditary Cancer Screening Folder</title>
<link href="https://fonts.googleapis.com/css2?family=Oswald:wght@400;500;600&family=Open+Sans:ital,wght@0,300;0,400;0,600;0,700;1,600&display=swap" rel="stylesheet">
<style>
:root{
  --bg:#ececec;
  --paper:#ffffff;
  --pocket:#cfe4f4;
  --brand-blue:#3a5b95;
  --accent-red:#e2392d;
  --ink:#2b2b2b;
  --muted:#8a8a8a;
  --cloud:#dde3ea;
  --wave:#eef4fa;
  --row-alt:#ececec;
  --lynch:#f7c143;
  --pj:#b3c93a;
  --lf:#3aa55a;
  --cowden:#2a9ad6;
  --hdgc:#5b5b5b;
}
*{margin:0;padding:0;box-sizing:border-box}
html,body{width:1200px;height:1000px;overflow:hidden;background:var(--bg)}
body{position:relative;font-family:"Open Sans",Arial,sans-serif;color:var(--ink)}
.dieline{position:absolute;left:0;top:0}
.abs{position:absolute}

/* back panel */
.back-brand{left:233px;top:216px;font-size:11px;letter-spacing:3px;color:var(--accent-red);font-weight:400}
.back-address{left:233px;top:233px;font-size:4.2px;line-height:6px;color:var(--muted);letter-spacing:.4px;width:160px}
.menu-title{left:417px;top:215px;font-size:11.5px;font-style:italic;font-weight:600;color:var(--accent-red)}
.menu-sub{left:440px;top:237px;font-size:4.2px;color:var(--muted);letter-spacing:.4px}
.gene-table{left:286px;top:259px;width:183px;border-collapse:collapse;background:var(--paper);box-shadow:2px 3px 5px rgba(0,0,0,.3);font-size:5px}
.gene-table td,.gene-table th{height:9.1px;padding:0 3px;text-align:left;white-space:nowrap;line-height:9px}
.gene-table th{background:var(--accent-red);color:#fff;font-weight:400}
.gene-table tr:nth-child(even) td{background:var(--row-alt)}
.gene-table .gene{color:var(--accent-red);font-weight:700;width:57px}
.gene-table .group td{color:#fff;background:var(--c)!important;padding-left:8px}
.gene-table .sub .gene{padding-left:8px}

/* front cover */
.wave-area{left:580px;top:560px;width:425px;height:98px;background:linear-gradient(180deg,rgba(238,244,250,0),var(--wave) 70%)}
.wave-area-back{left:143px;top:610px;width:437px;height:48px;background:linear-gradient(180deg,rgba(238,244,250,0),var(--wave))}
.logo{left:700px;top:193px;width:160px;text-align:center}
.logo-dot{display:block;width:20px;height:20px;border-radius:50%;background:var(--accent-red);margin:0 auto 6px}
.logo-name{font-size:10px;letter-spacing:3px;color:var(--brand-blue)}
.ribbon-row{left:733px;top:241px;width:107px;height:20px;border-radius:4px;
  background:linear-gradient(90deg,#f2b6cf 0%,#f6a75a 14%,#f6dc6a 26%,#9bd07f 38%,#6cbfe4 50%,#5a70bb 62%,#9d78c2 74%,#5a5a5a 86%,#bfd0e6 100%);
  box-shadow:0 1px 2px rgba(0,0,0,.15)}
.title{left:560px;top:278px;width:440px;text-align:center;font-family:"Oswald",sans-serif;font-weight:500;font-size:28px;line-height:34px;color:var(--brand-blue);letter-spacing:.1px}
.photo-couple{left:722px;top:315px;width:117px;height:117px;border-radius:50%;background:radial-gradient(circle at 45% 40%,#c9a088,#6d5a55 60%,#aab7c2)}
.word-cloud{left:632px;top:440px;width:300px;text-align:center;color:var(--cloud);font-weight:300;line-height:19.5px;white-space:nowrap}
.word-cloud span{margin:0 2px}
.power{left:600px;top:502px;width:360px;text-align:center;font-family:"Oswald",sans-serif;font-size:15px;letter-spacing:2.4px;color:var(--brand-blue);font-weight:500}
.photo-family{left:697px;top:529px;width:170px;height:96px;border-radius:50%;border:3px solid var(--brand-blue);background:linear-gradient(160deg,#eef1ee,#c8b79a 45%,#8d6c4d 80%,#d8cdb8)}
.tagline{left:620px;top:636px;width:320px;text-align:center;font-family:"Oswald",sans-serif;font-size:10px;letter-spacing:1.6px;color:var(--brand-blue)}

/* pockets (printed upside down so they read when folded) */
.pocket-copy{left:640px;top:732px;width:290px;transform:rotate(180deg);color:#fff;font-size:9.6px;line-height:12px}
.pocket-copy strong{font-weight:700}
.partner{left:295px;top:806px;width:160px;transform:rotate(180deg);color:#fff;font-size:7px;line-height:9px;text-align:left}
.partner strong{font-size:8px}
</style>
</head>
<body>
<svg class="dieline" width="1200" height="1000" viewBox="0 0 1200 1000">
  <path d="M143 170 L1005 170 L1005 462 A14 14 0 0 0 1005 490 L1005 658 L143 658 L143 490 A14 14 0 0 0 143 462 Z" fill="var(--paper)"/>
  <path d="M143 170 Q574 160 1005 170" stroke="#ddd" fill="none"/>
  <path d="M177 658 L562 658 L547 820 Q544 850 520 851 L177 851 Z" fill="var(--pocket)"/>
  <path d="M587 658 L972 658 L972 851 L632 851 Q606 850 603 820 Z" fill="var(--pocket)"/>
</svg>

<div class="abs wave-area-back" role="img" aria-label="Faint light blue wave pattern"></div>
<div class="abs wave-area" role="img" aria-label="Faint light blue wave pattern"></div>

<div class="abs back-brand">GENEVORA</div>
<div class="abs back-address">2200 HARLOW AVENUE NE | SUITE B | BROOKFIELD, GA 30000<br>(555) 010-2200 | (fax) 555 010-2201 | info@genevora.example</div>
<div class="abs menu-title">VELMORA TEST™ Menu</div>
<div class="abs menu-sub">CLIA: 00D0000000 | GENEVORA.EXAMPLE</div>

<table class="abs gene-table">
  <tr><th>GENE</th><th>CANCER-ASSOCIATED ORGAN/SYSTEMS</th></tr>
  <tr><td class="gene">APC</td><td>Colon</td></tr>
  <tr><td class="gene">ATM</td><td>Breast/Pancreatic/Brain</td></tr>
  <tr><td class="gene">BARD1</td><td>Breast/Ovarian</td></tr>
  <tr><td class="gene">BMPR1A</td><td>Colon</td></tr>
  <tr><td class="gene">BRCA1</td><td>Breast/Ovarian/Prostate</td></tr>
  <tr><td class="gene">BRCA2</td><td>Breast/Ovarian/Prostate</td></tr>
  <tr><td class="gene">BRIP1</td><td>Breast/Ovarian</td></tr>
  <tr><td class="gene">CDK4</td><td>Melanoma</td></tr>
  <tr><td class="gene">P16 (CDKN2A)</td><td>Melanoma/Breast/Pancreatic/Squamous</td></tr>
  <tr><td class="gene">FANCC</td><td>Blood</td></tr>
  <tr><td class="gene">MEN1</td><td>Thyroid/Parathyroid</td></tr>
  <tr><td class="gene">MET</td><td>Renal/Hepatic</td></tr>
  <tr><td class="gene">MRE11A</td><td>Ovarian/Breast</td></tr>
  <tr><td class="gene">NBN</td><td>Breast/Ovarian/Prostate/Melanoma</td></tr>
  <tr><td class="gene">NF1</td><td>Blood</td></tr>
  <tr><td class="gene">NTRK1</td><td>Thyroid/Parathyroid</td></tr>
  <tr><td class="gene">PALB2</td><td>Breast/Ovarian/Pancreatic</td></tr>
  <tr><td class="gene">PTCH1</td><td>Melanoma/Brain/Breast/Colon</td></tr>
  <tr><td class="gene">RAD50</td><td>Breast/Ovarian</td></tr>
  <tr><td class="gene">RAD51C</td><td>Ovarian/Breast</td></tr>
  <tr><td class="gene">RAD51D</td><td>Ovarian/Breast</td></tr>
  <tr><td class="gene">RET</td><td>Lung/Thyroid/Parathyroid</td></tr>
  <tr><td class="gene">SMAD4</td><td>Colon/Pancreas</td></tr>
  <tr class="group" style="--c:var(--lynch)"><td colspan="2">LYNCH SYNDROME GENES</td></tr>
  <tr class="sub"><td class="gene">MLH1</td><td>Colorectal/Ovarian</td></tr>
  <tr class="sub"><td class="gene">MSH2</td><td>Colorectal/Ovarian</td></tr>
  <tr class="sub"><td class="gene">MSH6</td><td>Colorectal/Ovarian</td></tr>
  <tr class="sub"><td class="gene">PMS2</td><td>Colorectal/Ovarian</td></tr>
  <tr class="sub"><td class="gene">EPCAM</td><td>Colorectal</td></tr>
  <tr class="group" style="--c:var(--pj)"><td colspan="2">PEUTZ-JEGHERS SYNDROME GENE</td></tr>
  <tr class="sub"><td class="gene">STK11</td><td>Breast/Ovarian/Melanoma/Colorectal/Lung</td></tr>
  <tr class="group" style="--c:var(--lf)"><td colspan="2">LI-FRAUMENI SYNDROME GENE</td></tr>
  <tr class="sub"><td class="gene">CHEK2</td><td>Breast/Ovarian/Prostate</td></tr>
  <tr class="sub"><td class="gene">PT53</td><td>Breast/Bladder/Ovarian/Squamous</td></tr>
  <tr class="group" style="--c:var(--cowden)"><td colspan="2">COWDEN SYNDROME GENE</td></tr>
  <tr class="sub"><td class="gene">PTEN</td><td>Endometrium/Breast/Prostate/Lung</td></tr>
  <tr class="group" style="--c:var(--hdgc)"><td colspan="2">HEREDITARY DIFFUSE GASTRIC CANCER SYNDROME GENE</td></tr>
  <tr class="sub"><td class="gene">CDH1</td><td>Breast/Gastric/Ovarian/Prostate</td></tr>
  <tr class="sub"><td class="gene">VHL</td><td>Renal</td></tr>
</table>

<div class="abs logo"><span class="logo-dot"></span><span class="logo-name">GENEVORA</span></div>
<div class="abs ribbon-row" role="img" aria-label="Row of cancer awareness ribbons in pink, orange, yellow, green, blue, purple, black and pale blue"></div>
<h1 class="abs title">Hereditary Cancer Screening</h1>
<div class="abs photo-couple" role="img" aria-label="Circular photo of a smiling couple embracing"></div>
<div class="abs word-cloud">
  <span style="font-size:14px">COLON</span><span style="font-size:20px">PANCREATIC</span><span style="font-size:14px">COLORECTAL</span><br>
  <span style="font-size:19px">ENDOMETRIAL</span><span style="font-size:13px">GASTRIC</span><span style="font-size:19px">OVARIAN</span><br>
  <span style="font-size:12px">BREAST</span><span style="font-size:17px">MELANOMA</span><span style="font-size:12px">LUNG</span><span style="font-size:18px">PROSTATE</span>
</div>
<div class="abs power">THE POWER OF KNOWLEDGE</div>
<div class="abs photo-family" role="img" aria-label="Oval photo of a family sharing a meal at a dining table"></div>
<div class="abs tagline">EASY + COMPREHENSIVE + FAST</div>

<div class="abs pocket-copy"><strong>At our state of the art,</strong> CLIA certified and COLA accredited facility we perform Next Generation Sequencing (NGS) based screening for mutations known to affect an individual's risk of developing Hereditary Cancer.<br>Results from the test enable the Physician to make better informed treatment decisions.</div>
<div class="abs partner"><strong>Orvell Health Partners</strong><br>an independent arm of Genevora LLC</div>
</body>
</html>
```